Redesign, cleanup and edit my Presentations

I have a series of power points that I use for training purposes. They were made by me over time. During the last couple years, I have evolved their look and content over time, but not consistently. More specifically, I have not gone back to re-edit the older decks. So, some decks are too wordy, too long, or and don't look consistent.

I am looking someone who can create a good design that I can use going forward, and who could also apply that theme to the existing decks, along with editing the existing, and future decks, too.

I have a lot of slides to produce and/or edit -approximately 500. But this request is a test to find a powerpoint partner. I am supplying 2 decks. One that's older and more wordy than the other. I would like to see what you would suggest we do differently. So that's what you are bidding on today. Also, you do not have to complete deck "Phase 4.7." I only need enough of the deck done to see where you would take it. Maybe 10 slides? Your choice. However, with that deck, there are lots of opportunities to clarify, re-align, and minimize within that deck.

But, if you are selected, I want to engage with you on an ongoing basis, and send more material your way. Then, you will be engaged to complete all decks.

Please ask me any questions to help you gain a better understanding of this project.

Target Market(s)

People in management, technical, medical, and financial fields who wish to become independent consultants.

Industry/Entity Type

Business Consultant

Font styles to use
Sans Serif

Requirements
Must have
• Use the existing color theme:
• yellow/gold - #f5b300,
• blue - 2b74a6
• Logo doesn't change
• Preferred fonts: Raleway for headings and Open Sans for general text
• Any pictures and graphics should have no copyright restrictions. That is, I should have use of the work without charge.
Nice to have
• I prefer a flat graphic style, although you can use pictures where it conveys a point more effectively.
• Ability to convert the presentations to Google Slides and Apple's Keynote apps.
• Ability to convert presentation to video
Should not have
• Restricted use graphics, photos, or other content.

```html
<!DOCTYPE html>
<html lang="en">
<head>
<meta charset="utf-8">
<title>Step 3.1 Personas – Deck Redesign</title>
<link href="https://fonts.googleapis.com/css2?family=Raleway:wght@500;700;800;900&family=Open+Sans:wght@400;600;700&display=swap" rel="stylesheet">
<style>
:root{
  --gold:#f5b300;
  --gold-soft:#fcd566;
  --blue:#2b74a6;
  --blue-dark:#1d5a85;
  --blue-pale:#dbe9f3;
  --ink:#3a3f45;
  --grey:#8a9097;
  --page:#e9edf1;
  --white:#ffffff;
}
*{box-sizing:border-box;margin:0;padding:0}
html,body{width:1200px;height:3012px;overflow:hidden;background:var(--page)}
body{font-family:"Open Sans",Arial,sans-serif;color:var(--ink)}
.sheet{
  width:1200px;height:3012px;padding:8px;
  display:grid;grid-template-columns:584px 584px;
  grid-template-rows:repeat(8,328px) 244px;gap:16px;
}
.slide{position:relative;background:var(--white);overflow:hidden;box-shadow:0 1px 3px rgba(0,0,0,.18)}
h1,h2,h3{font-family:"Raleway",Arial,sans-serif}
.brand{position:absolute;top:10px;right:14px;display:flex;align-items:center;gap:5px;
  font-family:"Open Sans",Arial,sans-serif;font-weight:700;font-size:12px;color:var(--blue)}
.brand i{width:9px;height:9px;border-radius:50%;background:var(--gold);display:block}
.rule{position:absolute;left:0;right:0;bottom:0;height:8px;background:var(--blue)}
.rule::after{content:"";position:absolute;right:0;top:0;width:30%;height:100%;background:var(--gold)}
.head{height:46px;background:var(--blue);display:flex;align-items:center;padding:0 22px}
.head h2{color:var(--white);font-size:21px;font-weight:800;letter-spacing:.5px}
.small{font-size:9.5px;line-height:1.45}
.body{padding:14px 24px}
ul.dots{list-style:none}
ul.dots li{position:relative;padding-left:14px;margin-bottom:7px;font-size:10px;line-height:1.45}
ul.dots li::before{content:"";position:absolute;left:0;top:5px;width:6px;height:6px;background:var(--gold);border-radius:50%}
/* step slides */
.step-band{position:absolute;left:0;top:24px;width:400px;height:58px;background:var(--gold);display:flex;align-items:center;padding-left:24px}
.step-band h2{color:var(--white);font-size:24px;font-weight:800}
.step-box{position:absolute;right:34px;top:14px;width:110px;height:78px;background:var(--blue);color:var(--white);
  font-family:"Raleway",Arial,sans-serif;display:flex;align-items:center;justify-content:center;gap:8px}
.step-box span{font-size:15px;font-weight:700;writing-mode:vertical-rl;transform:rotate(180deg)}
.step-box b{font-size:52px;font-weight:800;line-height:1}
.step-body{position:absolute;left:24px;right:24px;top:108px}
.ph{display:block}
/* title slide */
.title-photo{position:absolute;inset:0 0 70px 0;background:linear-gradient(180deg,#9cb9cf 0%,#c7b48a 55%,#6d6a5a 100%)}
.title-card{position:absolute;left:26px;top:26px;width:220px;height:120px;background:var(--gold);padding:16px 20px}
.title-card h1{color:var(--white);font-size:34px;font-weight:800;line-height:1.05}
.title-card p{color:var(--white);font-family:"Raleway",Arial,sans-serif;font-weight:700;font-size:18px;letter-spacing:2px;margin-top:6px}
.title-foot{position:absolute;left:0;right:0;bottom:0;height:70px;display:flex;align-items:center;padding-left:30px;gap:8px;
  color:var(--blue);font-weight:700;font-size:24px}
.title-foot i{width:18px;height:18px;border-radius:50%;background:var(--gold);display:block}
.title-foot::after{content:"";position:absolute;right:0;top:0;width:8px;height:100%;background:var(--blue)}
/* journey */
.big-title{padding:14px 22px 0;font-family:"Raleway",Arial,sans-serif;font-size:24px;font-weight:800;color:var(--blue)}
.big-title em{font-style:normal;color:var(--gold)}
/* table */
.grid-table{width:100%;border-collapse:collapse;font-size:8.5px}
.grid-table th{background:var(--gold);color:var(--white);padding:5px;text-align:left;font-weight:700}
.grid-table td{border:1px solid #c9d6e0;padding:5px;background:#f4f8fb}
/* characteristics */
.traits{display:flex;gap:12px;padding:30px 26px 0;justify-content:center}
.trait{width:112px;height:118px;background:var(--blue);color:var(--white);font-size:11px;font-weight:700;
  display:flex;align-items:center;justify-content:center;text-align:center;padding:10px;position:relative}
.trait::after{content:"";position:absolute;left:0;right:0;bottom:-10px;height:10px;background:var(--gold)}
.trait:nth-child(even){margin-top:22px}
/* persona sheet */
.persona-photo{position:absolute;left:0;top:0;width:150px;height:150px;background:linear-gradient(160deg,#c9d9e6,#8fb0c8)}
.persona-name{position:absolute;left:0;top:150px;width:150px;height:38px;background:var(--gold);color:var(--white);
  font-family:"Raleway",Arial,sans-serif;font-weight:800;font-size:17px;display:flex;align-items:center;padding-left:12px}
.persona-brief{position:absolute;left:0;top:188px;width:150px;bottom:0;background:var(--blue);color:var(--white);padding:10px 12px;font-size:8px;line-height:1.45}
.persona-cols{position:absolute;left:166px;right:14px;top:30px;display:grid;grid-template-columns:1fr 1fr;gap:10px 16px}
.persona-cols h3{font-size:11px;color:var(--blue);font-weight:800;margin-bottom:3px}
.persona-cols p{font-size:8px;line-height:1.4}
/* five rings */
.rings{position:absolute;left:24px;right:24px;top:150px;display:flex;justify-content:space-between}
.ring{width:88px;text-align:center}
.ring b{display:flex;width:52px;height:52px;margin:0 auto 8px;border-radius:50%;border:4px solid var(--blue);
  align-items:center;justify-content:center;font-family:"Raleway",Arial,sans-serif;font-size:20px;color:var(--blue)}
.ring:nth-child(even) b{border-color:var(--gold);color:var(--gold)}
.ring span{font-size:9px;font-weight:600;color:var(--ink)}
/* template */
.template{background:var(--gold);display:flex;align-items:center;justify-content:center;text-align:center}
.template h1{color:var(--white);font-size:38px;font-weight:800;line-height:1.1;letter-spacing:1px}
.template-note{display:flex;align-items:center;padding:0 60px 0 250px}
.template-note p{font-size:13px;line-height:1.6;color:var(--ink)}
.template-note p b{color:var(--blue)}
</style>
</head>
<body>
<main class="sheet">

  <!-- 1 Title -->
  <section class="slide">
    <div class="title-photo ph" role="img" aria-label="Photo of an open road stretching toward the horizon"></div>
    <div class="title-card"><h1>Step 3.1</h1><p>PERSONAS</p></div>
    <div class="title-foot"><i></i>Vantora</div>
  </section>

  <!-- 2 Customer journey map -->
  <section class="slide">
    <div class="brand"><i></i>Vantora</div>
    <h2 class="big-title">CUSTOMER JOURNEY <em>MAP</em></h2>
    <svg width="584" height="250" viewBox="0 0 584 250" aria-label="Loop of journey stages joined by arrows">
      <g fill="none" stroke="var(--blue)" stroke-width="14" stroke-linecap="round">
        <path d="M150 120 C150 40 420 40 430 110"/>
        <path d="M430 150 C420 220 160 220 150 160"/>
      </g>
      <path d="M418 100 l24 12 l-2 -26z" fill="var(--blue)"/>
      <path d="M162 170 l-24 -10 l2 26z" fill="var(--blue)"/>
      <g font-family="Open Sans,Arial,sans-serif" font-size="10" font-weight="700" fill="var(--white)">
        <rect x="40" y="110" width="96" height="30" fill="var(--gold)"/><text x="88" y="129" text-anchor="middle">Awareness</text>
        <rect x="240" y="20" width="96" height="30" fill="var(--gold)"/><text x="288" y="39" text-anchor="middle">Consideration</text>
        <rect x="450" y="110" width="96" height="30" fill="var(--gold)"/><text x="498" y="129" text-anchor="middle">Purchase</text>
        <rect x="240" y="200" width="96" height="30" fill="var(--gold)"/><text x="288" y="219" text-anchor="middle">Loyalty</text>
      </g>
      <circle cx="290" cy="128" r="34" fill="var(--blue-pale)"/>
      <text x="290" y="132" text-anchor="middle" font-family="Raleway,Arial,sans-serif" font-weight="800" font-size="11" fill="var(--blue)">PERSONA</text>
    </svg>
    <div class="rule"></div>
  </section>

  <!-- 3 B2C personas -->
  <section class="slide">
    <div class="head"><h2>B2C PERSONAS</h2></div>
    <div class="brand" style="color:var(--white)"><i></i>Vantora</div>
    <div class="body">
      <p class="small">A persona is a short profile of the person you most want to serve. It gathers what they value, how they decide and what blocks them, so every message you write speaks to one real reader instead of a crowd.</p>
    </div>
    <div class="ph" role="img" aria-label="Flat illustration of three smiling people" style="position:absolute;left:150px;right:150px;top:130px;height:150px;background:linear-gradient(180deg,#fbe3a0,#f5c94a)"></div>
    <p style="position:absolute;left:24px;bottom:20px;font-size:10px;font-weight:700;color:var(--blue)">Consumer</p>
    <div class="rule"></div>
  </section>

  <!-- 4 Our B2C persona focus -->
  <section class="slide">
    <div class="head"><h2>OUR B2C PERSONA FOCUS</h2></div>
    <div class="brand" style="color:var(--white)"><i></i>Vantora</div>
    <div class="body">
      <table class="grid-table">
        <tr><th>Who we focus on and why it matters for the plan</th></tr>
        <tr><td>Mid-career professionals ready to leave a salaried role and sell their skills directly.</td></tr>
        <tr><td>They want freedom of schedule, fair pay and work that uses their full expertise.</td></tr>
        <tr><td>Main worry: finding the first clients and pricing services with confidence.</td></tr>
        <tr><td>They trust peers, short case studies and clear, practical next steps.</td></tr>
        <tr><td>Best reached through referrals, local groups and targeted online content.</td></tr>
      </table>
    </div>
    <div class="rule"></div>
  </section>

  <!-- 5 B2C characteristics -->
  <section class="slide">
    <div class="head"><h2>B2C CHARACTERISTICS</h2></div>
    <div class="brand" style="color:var(--white)"><i></i>Vantora</div>
    <div class="traits">
      <div class="trait">Purchases are often emotional</div>
      <div class="trait">Purchases are made by one person</div>
      <div class="trait">Sales cycles are short and simple</div>
      <div class="trait">Purchases can be impulsive</div>
    </div>
    <div class="rule"></div>
  </section>

  <!-- 6 When you know it's right -->
  <section class="slide">
    <div class="head"><h2>WHEN YOU KNOW IT'S RIGHT</h2></div>
    <div class="brand" style="color:var(--white)"><i></i>Vantora</div>
    <div class="body">
      <p style="font-size:11px;font-weight:700;color:var(--gold);margin-bottom:8px">When you start to say their things are, like, "Oh yeah…"</p>
      <ul class="dots">
        <li>They all answer the same question the same way</li>
        <li>They all navigate the buyer's journey the same</li>
        <li>They all have these goals</li>
        <li>They are all around this same age</li>
        <li>They live in the same region</li>
        <li>They all have the same challenges</li>
        <li>They're all from the same part of the country</li>
      </ul>
      <p class="small" style="margin-top:4px">Whatever it is. When you start to see these common things line up, that is when you know you're on the right track.</p>
    </div>
    <div class="rule"></div>
  </section>

  <!-- 7 Step 1 -->
  <section class="slide">
    <div class="step-band"><h2>Build a Background Profile</h2></div>
    <div class="step-box"><span>STEP</span><b>1</b></div>
    <ul class="dots step-body">
      <li>Background, or demographics, is basic information the business can use for the persona.</li>
      <li>For B2C personas this can include age, gender, marital status, geographic location, education level and income. Use one or two sources that you trust.</li>
      <li>Start with your marketing research, interviews or surveys. Confirm what you can and note what you still assume.</li>
      <li>Be specific enough that you can visualize the persona, but not so detailed that you limit who it represents.</li>
    </ul>
    <div class="rule"></div>
  </section>

  <!-- 8 Step 2 -->
  <section class="slide">
    <div class="step-band"><h2>Naming and Photo</h2></div>
    <div class="step-box"><span>STEP</span><b>2</b></div>
    <ul class="dots step-body">
      <li>Adding a name helps to humanize the persona, making it feel like a real individual.</li>
      <li>A photo puts a face to the name and makes it easier to visualize who you are writing for.</li>
      <li>A shared name also creates a common language the team can use in every meeting.</li>
      <li>Avoid naming the persona after someone you already know.</li>
    </ul>
    <div class="rule"></div>
  </section>

  <!-- 9 Step 3 -->
  <section class="slide">
    <div class="step-band"><h2>Financial Situation</h2></div>
    <div class="step-box"><span>STEP</span><b>3</b></div>
    <div class="rule"></div>
  </section>

  <!-- 10 Step 4 -->
  <section class="slide">
    <div class="step-band"><h2>Day in the life</h2></div>
    <div class="step-box"><span>STEP</span><b>4</b></div>
    <p class="small step-body" style="color:var(--grey)">Describe a typical day from morning to evening: where they work, who they talk to and when they have time to look for help.</p>
    <div class="rule"></div>
  </section>

  <!-- 11 Persona sheet -->
  <section class="slide">
    <div class="persona-photo ph" role="img" aria-label="Portrait photo of the persona"></div>
    <div class="persona-name">DANA MORRIS</div>
    <div class="persona-brief">Brief bio: finance manager, 44, planning to launch an advisory practice within the next year.</div>
    <div class="brand"><i></i>Vantora</div>
    <div class="persona-cols">
      <div><h3>Background</h3><p>Age 44, married, two children. Suburban home, 20 years in corporate finance.</p></div>
      <div><h3>Hopes &amp; Dreams</h3><p>Own schedule, steady clients, work she is proud of.</p></div>
      <div><h3>What she looks for</h3><p>Clear steps, proven methods and honest pricing advice.</p></div>
      <div><h3>Brand Affinities</h3><p>Business podcasts, trade journals, local networking events.</p></div>
      <div><h3>What influences her?</h3><p>Peers, former colleagues and short real-world case studies.</p></div>
      <div><h3>What can we do?</h3><p>Offer a starter plan and a simple pricing worksheet.</p></div>
      <div><h3>Worries &amp; Fears</h3><p>Losing a stable income and not finding clients fast enough.</p></div>
      <div><h3>Objections</h3><p>Cost of training and time away from her current job.</p></div>
    </div>
    <div class="rule"></div>
  </section>

  <!-- 12 B2B personas -->
  <section class="slide">
    <div class="head"><h2>B2B PERSONAS</h2></div>
    <div class="brand" style="color:var(--white)"><i></i>Vantora</div>
    <div style="text-align:center;padding-top:34px">
      <p style="font-size:13px">Tells us what prospective customers</p>
      <p style="font-family:Raleway,Arial,sans-serif;font-weight:800;font-size:24px;color:var(--blue);line-height:1.15;margin:6px 0">think<br>do<br>want<br>need</p>
      <p style="font-size:11px;line-height:1.5">as they weigh their options.<br>This is usually a team, and the better we understand the team,<br>the better we know how to communicate to them.</p>
    </div>
    <div class="rule"></div>
  </section>

  <!-- 13 The hard work -->
  <section class="slide">
    <div class="head"><h2>THE HARD WORK</h2></div>
    <div class="brand" style="color:var(--white)"><i></i>Vantora</div>
    <div class="body">
      <p class="small" style="text-align:center;margin-bottom:12px">Talk to real buyers. Interview recent clients, lost prospects and partners to learn what triggered their search and what finally made them decide.</p>
      <div style="display:grid;grid-template-columns:1fr 1fr;gap:20px">
        <div>
          <svg width="34" height="34" viewBox="0 0 34 34" aria-hidden="true"><circle cx="17" cy="17" r="16" fill="var(--gold)"/><path d="M10 18l5 5 9-11" stroke="#fff" stroke-width="3" fill="none"/></svg>
          <p style="font-size:10px;font-weight:700;color:var(--blue);margin:4px 0">Triggers for the conversation</p>
          <ul class="dots"><li>Budget and deadlines</li><li>Changes in leadership</li><li>New rules or processes</li></ul>
        </div>
        <div>
          <svg width="34" height="34" viewBox="0 0 34 34" aria-hidden="true"><circle cx="17" cy="17" r="16" fill="var(--blue)"/><path d="M17 9v10M17 23v2" stroke="#fff" stroke-width="3"/></svg>
          <p style="font-size:10px;font-weight:700;color:var(--blue);margin:4px 0">Research styles</p>
          <ul class="dots"><li>Search and reading</li><li>Blogs and peers</li><li>Vendor meetings</li></ul>
        </div>
      </div>
    </div>
    <div class="rule"></div>
  </section>

  <!-- 14 Five rings -->
  <section class="slide">
    <div class="step-band" style="width:440px"><h2>KNOW THE FIVE RINGS OF BUYER INSIGHT</h2></div>
    <div class="step-box"><span>STEP</span><b>1</b></div>
    <div class="rings">
      <div class="ring"><b>01</b><span>Priority Initiatives</span></div>
      <div class="ring"><b>02</b><span>Success Factors</span></div>
      <div class="ring"><b>03</b><span>Perceived Barriers</span></div>
      <div class="ring"><b>04</b><span>Buyer's Journey</span></div>
      <div class="ring"><b>05</b><span>Decision Criteria</span></div>
    </div>
    <div class="rule"></div>
  </section>

  <!-- 15 Priority initiatives -->
  <section class="slide">
    <div class="head"><h2>PRIORITY INITIATIVES</h2></div>
    <div class="brand" style="color:var(--white)"><i></i>Vantora</div>
    <div class="body">
      <p class="small" style="margin-bottom:10px">What moves a buyer to act now? Find the problem or goal that makes them set aside time and budget for a solution like yours.</p>
      <div style="display:grid;grid-template-columns:40px 1fr;gap:10px 12px;align-items:center">
        <svg width="36" height="36" viewBox="0 0 36 36" aria-hidden="true"><circle cx="18" cy="18" r="17" fill="var(--gold)"/><path d="M11 18h14M19 12l6 6-6 6" stroke="#fff" stroke-width="3" fill="none"/></svg>
        <p class="small">The trigger is any event that creates urgency, such as a new goal, a failed project or a change in leadership.</p>
        <svg width="36" height="36" viewBox="0 0 36 36" aria-hidden="true"><circle cx="18" cy="18" r="17" fill="var(--blue)"/><path d="M11 18l5 5 9-11" stroke="#fff" stroke-width="3" fill="none"/></svg>
        <p class="small">Understand why some buyers stay with what they have and what it takes to change their mind.</p>
        <svg width="36" height="36" viewBox="0 0 36 36" aria-hidden="true"><circle cx="18" cy="18" r="17" fill="var(--gold)"/><circle cx="18" cy="18" r="6" fill="#fff"/></svg>
        <p class="small">Ask what they hoped to fix and what would have happened if they did nothing at all.</p>
      </div>
    </div>
    <div class="rule"></div>
  </section>

  <!-- 16 Closing question -->
  <section class="slide">
    <div style="position:absolute;left:0;top:60px;width:14px;height:130px;background:var(--gold)"></div>
    <h1 style="position:absolute;left:40px;right:40px;top:60px;font-size:27px;font-weight:900;color:var(--blue);line-height:1.2">DO YOU HAVE THE RIGHT MESSAGES THAT WILL ATTRACT YOUR PERSONA(S)?</h1>
    <div style="position:absolute;left:0;right:0;top:216px;height:48px;background:var(--blue);display:flex;align-items:center;padding-left:40px">
      <p style="color:var(--white);font-size:15px;font-weight:600">What we'll answer in the next lesson.</p>
    </div>
    <div class="rule"></div>
  </section>

  <!-- 17 Template -->
  <section class="slide template">
    <h1>B2B<br>PERSONA<br>TEMPLATE</h1>
  </section>
  <section class="slide template-note">
    <p>The next two slides are an example of a business buyer persona.<br><br><b>Use</b> the categories and prompts to guide you to what to capture.<br><br><b>Replace</b> categories and text as it is relevant to your market.</p>
  </section>

</main>
</body>
</html>
```